We need an attractive business card design that is modern and inviting. We like the blue and yellow (or gold) colors that are displayed with the logo. The business should communicate trust, experience, and integrity.

Target Market(s)

Residential and Commercial

Industry/Entity Type

Business

Contact Information for Business Card

Recessed Lighting
LED Retro Fit
Sign Repair
Alarms and Cameras
Mobile Home Services
24hr service calls

Font styles to use
Serif
Sans Serif

Colors
3176b5
0455a3
fece3e
fbee3e

Requirements
Must have
• Brannick Electric
• Owner: Marcus Brannick
• Licensed and Insured
• TECL #58731
Nice to have
• Exquisite Detail!!
• Over 20 years of experience
Should not have
• Nothing boring or traditional!!!

```html
<!DOCTYPE html>
<html lang="en">
<head>
<meta charset="utf-8">
<title>Brannick Electric – Business Card</title>
<link rel="stylesheet" href="https://fonts.googleapis.com/css2?family=Open+Sans:wght@400;600;700;800&display=swap">
<style>
  :root {
    --blue-light: #3176b5;
    --blue-deep: #0455a3;
    --gold: #fece3e;
    --yellow: #fbee3e;
    --white: #ffffff;
    --ink: #2b2b2b;
    --grey: #a9a9a9;
    --stage: #2e2e2e;
  }
  html, body {
    margin: 0;
    padding: 0;
    width: 1200px;
    height: 900px;
    overflow: hidden;
    background: var(--stage);
    font-family: "Open Sans", Arial, sans-serif;
  }
  .canvas {
    position: relative;
    width: 1200px;
    height: 900px;
    display: flex;
    align-items: center;
    justify-content: center;
    gap: 54px;
  }
  .card {
    position: relative;
    width: 520px;
    height: 298px;
    border-radius: 22px;
    overflow: hidden;
    box-shadow: 0 18px 40px rgba(0,0,0,.45);
  }
  .card svg.card-art {
    position: absolute;
    inset: 0;
    width: 100%;
    height: 100%;
  }
  /* Front face */
  .card--front { background: var(--white); }
  .owner-name {
    position: absolute;
    left: 118px;
    top: 44px;
    margin: 0;
    font-size: 25px;
    font-weight: 800;
    letter-spacing: .5px;
    color: var(--blue-deep);
    text-transform: uppercase;
  }
  .owner-role {
    position: absolute;
    left: 118px;
    top: 76px;
    margin: 0;
    font-size: 13px;
    font-weight: 600;
    color: var(--grey);
    text-transform: uppercase;
  }
  .brand-mark {
    position: absolute;
    left: 40px;
    top: 104px;
    display: flex;
    align-items: center;
    gap: 8px;
  }
  .brand-dot {
    width: 56px;
    height: 56px;
    border-radius: 50%;
    border: 5px solid var(--blue-deep);
    box-sizing: border-box;
  }
  .contact-list {
    position: absolute;
    left: 118px;
    top: 112px;
    margin: 0;
    padding: 0;
    list-style: none;
    font-size: 13.5px;
    line-height: 20px;
    color: var(--ink);
  }
  .contact-list b { font-weight: 700; }
  .license-block {
    position: absolute;
    right: 96px;
    bottom: 74px;
    font-size: 13px;
    font-weight: 700;
    line-height: 18px;
    color: var(--ink);
    letter-spacing: .4px;
    text-align: left;
  }
  /* Back face */
  .card--back { background: var(--blue-light); }
  .service-list {
    position: absolute;
    left: 64px;
    top: 36px;
    margin: 0;
    padding: 0;
    list-style: none;
    font-size: 12.5px;
    line-height: 17px;
    color: var(--white);
  }
  .service-list li {
    display: flex;
    align-items: center;
    gap: 8px;
  }
  .tick { width: 11px; height: 9px; flex: none; }
  .company-lockup {
    position: absolute;
    right: 44px;
    top: 156px;
    text-align: right;
  }
  .company-row {
    display: flex;
    align-items: center;
    justify-content: flex-end;
    gap: 10px;
  }
  .company-name {
    margin: 0;
    font-size: 28px;
    font-weight: 800;
    color: var(--yellow);
    text-transform: uppercase;
    letter-spacing: 1px;
  }
  .company-dot {
    width: 40px;
    height: 40px;
    border-radius: 50%;
    border: 4px solid var(--blue-deep);
    box-sizing: border-box;
  }
  .company-web {
    margin: 6px 0 0;
    font-size: 13px;
    color: var(--white);
    letter-spacing: .3px;
  }
</style>
</head>
<body>
<main class="canvas">

  <!-- Front face -->
  <section class="card card--front" aria-label="Business card front">
    <svg class="card-art" viewBox="0 0 520 298" aria-hidden="true">
      <defs>
        <path id="license-curve" d="M330,14 C390,30 430,90 470,170 C485,200 500,215 520,222"/>
      </defs>
      <path d="M0,0 H260 C200,26 120,34 0,38 Z" fill="var(--blue-deep)"/>
      <path d="M250,0 H520 V240 C470,220 440,160 410,100 C380,40 320,12 250,0 Z" fill="var(--yellow)"/>
      <path d="M300,0 H520 V240 C490,230 465,190 440,130 C410,60 370,20 300,0 Z" fill="var(--gold)"/>
      <path d="M0,150 C50,160 85,220 105,298 H0 Z" fill="var(--gold)"/>
      <path d="M0,200 C35,210 60,250 72,298 H0 Z" fill="var(--yellow)"/>
      <path d="M80,298 C120,250 180,236 250,244 C340,256 430,268 520,232 V298 Z" fill="var(--blue-deep)"/>
      <text font-family="Open Sans, Arial, sans-serif" font-size="13" font-weight="700" fill="#ffffff" letter-spacing="2">
        <textPath href="#license-curve" startOffset="28%">Licensed and Insured</textPath>
      </text>
    </svg>
    <h1 class="owner-name">Marcus Brannick</h1>
    <p class="owner-role">Owner</p>
    <div class="brand-mark"><span class="brand-dot"></span></div>
    <ul class="contact-list">
      <li><b>P :</b> 936-555-0147</li>
      <li><b>E :</b> mbrannick@mailhaven.com</li>
      <li><b>A :</b> Harlow Springs, Texas</li>
    </ul>
    <div class="license-block">
      <div>TECL: 58731</div>
      <div>Security: B47315</div>
    </div>
  </section>

  <!-- Back face -->
  <section class="card card--back" aria-label="Business card back">
    <svg class="card-art" viewBox="0 0 520 298">
      <rect x="0" y="0" width="520" height="298" fill="var(--blue-light)" role="img" aria-label="Faint world map texture behind the card content"/>
      <path d="M0,0 H330 C260,10 140,14 0,20 Z" fill="var(--blue-deep)" aria-hidden="true"/>
      <path d="M300,0 H520 V130 C490,120 460,90 430,55 C400,20 360,6 300,0 Z" fill="var(--gold)" aria-hidden="true"/>
      <path d="M340,0 H520 V95 C495,88 470,60 450,38 C420,10 390,4 340,0 Z" fill="var(--yellow)" aria-hidden="true"/>
      <path d="M0,118 C70,120 120,170 150,250 L158,298 H0 Z" fill="var(--gold)" aria-hidden="true"/>
      <path d="M0,150 C55,156 95,200 112,260 L120,298 H0 Z" fill="var(--yellow)" aria-hidden="true"/>
      <path d="M130,298 C150,250 190,232 250,240 C340,252 440,250 520,225 V298 Z" fill="var(--blue-deep)" aria-hidden="true"/>
    </svg>
    <ul class="service-list">
      <li><svg class="tick" viewBox="0 0 11 9" aria-hidden="true"><path d="M1,5 L4,8 L10,1" fill="none" stroke="#fff" stroke-width="2"/></svg>Residential and Commercial</li>
      <li><svg class="tick" viewBox="0 0 11 9" aria-hidden="true"><path d="M1,5 L4,8 L10,1" fill="none" stroke="#fff" stroke-width="2"/></svg>Recessed Lighting</li>
      <li><svg class="tick" viewBox="0 0 11 9" aria-hidden="true"><path d="M1,5 L4,8 L10,1" fill="none" stroke="#fff" stroke-width="2"/></svg>LED Retro Fit</li>
      <li><svg class="tick" viewBox="0 0 11 9" aria-hidden="true"><path d="M1,5 L4,8 L10,1" fill="none" stroke="#fff" stroke-width="2"/></svg>Sign Repair</li>
      <li><svg class="tick" viewBox="0 0 11 9" aria-hidden="true"><path d="M1,5 L4,8 L10,1" fill="none" stroke="#fff" stroke-width="2"/></svg>Alarms and Cameras</li>
      <li><svg class="tick" viewBox="0 0 11 9" aria-hidden="true"><path d="M1,5 L4,8 L10,1" fill="none" stroke="#fff" stroke-width="2"/></svg>Mobile Home Service</li>
      <li><svg class="tick" viewBox="0 0 11 9" aria-hidden="true"><path d="M1,5 L4,8 L10,1" fill="none" stroke="#fff" stroke-width="2"/></svg>24hr service calls</li>
    </ul>
    <div class="company-lockup">
      <div class="company-row">
        <h2 class="company-name">Brannick Electric</h2>
        <span class="company-dot"></span>
      </div>
      <p class="company-web">www.brannickelectric.com</p>
    </div>
  </section>

</main>
</body>
</html>
```